Aviation: Overcast Study Guide Book Cover

We need a book cover (front and back) designed for an Instrument Flight Rules (IFR) study guide used by helicopter and airplane pilots to obtain an instrument rating for a helicopter or airplane. Below is the title and subtitles.

TITLE: OVERCAST STUDY GUIDE
SUBTITLE 1: Checkride Preparation for Airplane and Helicopter Pilots
SUBTITLE 2: Prepare for your Instrument Rating with Confidence

We have also upload recommended text to be included on the back cover. In addition, we included images of similar book covers that we like and ones that we do not like. Below are links to two others books by the author.

https://www.bookvarro.example/Rotorcraft-Exam-Handbook-oral-review/dp/507214638K
https://www.bookvarro.example/Manual-Floatwing-Handling-Lionel-Quarrick/dp/5093742816

Flight students

Aviation

• helicopter and airplane

```html
<!DOCTYPE html>
<html lang="en">
<head>
<meta charset="utf-8">
<title>Overcast Study Guide – Book Cover</title>
<link rel="stylesheet" href="https://fonts.googleapis.com/css2?family=Montserrat:wght@500;600;700;800&display=swap">
<style>
  :root {
    --backdrop: #e9e9e9;
    --cover-dark: #0d0606;
    --sky-blue: #2f56d8;
    --sky-light: #a9c6ee;
    --glow-orange: #d7821e;
    --title-orange: #f07a0c;
    --title-white: #f2f2f2;
    --tagline-ink: #1a1d2a;
    --band-orange: #f27c10;
  }
  * { margin: 0; padding: 0; box-sizing: border-box; }
  html, body {
    width: 1200px; height: 1200px; overflow: hidden;
    background: var(--backdrop);
    font-family: "Montserrat", sans-serif;
  }
  .cover {
    position: absolute; left: 239px; top: 40px;
    width: 722px; height: 1120px;
    background: var(--cover-dark);
    overflow: hidden;
  }
  .cover-photo {
    position: absolute; inset: 0 0 380px 0;
    background:
      radial-gradient(ellipse 55% 40% at 8% 62%, rgba(230,150,40,0.85), rgba(230,150,40,0) 70%),
      linear-gradient(200deg, var(--sky-blue) 0%, var(--sky-light) 22%, rgba(60,45,35,0.9) 40%, #3a2a1f 60%, var(--cover-dark) 100%);
  }
  .cover-photo::after {
    content: ""; position: absolute; inset: 0;
    background: linear-gradient(180deg, rgba(13,6,6,0) 55%, var(--cover-dark) 100%);
  }
  .tagline {
    position: absolute; left: 237px; top: 160px;
    white-space: nowrap;
    transform: rotate(-32deg); transform-origin: left top;
    color: var(--tagline-ink);
    font-weight: 600; font-size: 18px; line-height: 1.4;
    letter-spacing: 1.5px; text-transform: uppercase;
  }
  .title-block {
    position: absolute; left: 106px; top: 462px;
  }
  .author {
    color: var(--title-white); font-weight: 600;
    font-size: 38px; letter-spacing: 0.5px;
  }
  .title-main {
    display: block;
    color: var(--title-orange); font-weight: 800;
    font-size: 96px; line-height: 1; margin-top: 18px; letter-spacing: 2px;
  }
  .title-sub {
    display: block;
    color: var(--title-white); font-weight: 800;
    font-size: 108px; line-height: 1.02; letter-spacing: 3px;
  }
  .title-main + .title-sub { margin-top: 14px; }
  .checkride-band {
    position: absolute; left: 76px; right: 0; top: 938px; height: 66px;
    background: linear-gradient(90deg, var(--band-orange) 0%, rgba(242,124,16,0.6) 45%, rgba(120,50,10,0.25) 100%);
    padding: 8px 0 0 14px;
    color: #fbe9dc; font-weight: 600; font-size: 20px;
    line-height: 1.3; letter-spacing: 2px; text-transform: uppercase;
  }
</style>
</head>
<body>
  <main class="cover">
    <div class="cover-photo" role="img" aria-label="Pilot's arm on the controls in a cockpit, flight instruments and sunlit sky through the windscreen"></div>
    <p class="tagline">Prepare for your<br>instrument rating<br>with confidence</p>
    <div class="title-block">
      <p class="author">LIONEL J. QUARRICK</p>
      <h1>
        <span class="title-main">OVERCAST</span>
        <span class="title-sub">STUDY</span>
        <span class="title-sub">GUIDE</span>
      </h1>
    </div>
    <p class="checkride-band">Checkride preparation for<br>airplane and helicopter pilots</p>
  </main>
</body>
</html>
```